Design a Flyer for LIVE Real Estate Event

Submit Your Best Flyer Design Entry to Promote An Upcoming LIVE Event;

How To Find Money Making Properties at the Auction

LIVE Event

Hosted by Dalton Preswick from Brickline Holdings TV

Who?

Hosts:
Dalton Preswick
Real Estate Investor since 2001 flipped over 100 properties.

Owen Lathey
Founder of KEYSTONE GRAB & Real Estate Auction Buyer Since 2011 Buying over 350 Properties

Guests/Panel:
Real Estate Attorneys
Real Estate Agents
Member Testimonials

What?
How To Search Properties on County Site
How To Determine If The Property Is Worth Further Research
How To Navigate From KEYSTONE GRAB Site to 3rd Party Sites
How To Find Total HOA Assessments
How To Find Total Mortgage Debt
How To Find Taxes Due
How To Find Other Foreclosure Cases
How To Determine Market Value
How To Find Other Liens
How To Search Properties on Gavelor AI
Why You Should Order Report

How To Take Possession of The Property
How To Deal with Tenants
How To Deal with Associations
How To Deal with Banks
How To Rent The Property Quickly
How To Sell The Property Fast
How To Rehab the Property Fast & On A Budget
Where? TBA

When? 3/16-3/18, 3/23-3/25, 3/30-4/1

Why? Learn How To Make Big Money with Foreclosure Auctions

How? Sign up on keystonegrab.example, BricklineHoldingsTV.example

Day 1 - Property Research
Day 2 - Property Management
Day 3 - Gavelor AI Demo, KEYSTONE GRAB Members, BricklineHoldings TV Coaching Packages

```html
<!DOCTYPE html>
<html lang="en">
<head>
<meta charset="utf-8">
<title>Live Event – Foreclosure Auctions Flyer</title>
<link rel="stylesheet" href="https://fonts.googleapis.com/css2?family=Montserrat:wght@400;500;600;700&family=Open+Sans:wght@400;500&display=swap">
<style>
  :root {
    --navy: #0e3a6e;
    --panel: #eceeef;
    --white: #ffffff;
    --ink: #1a1a1a;
    --muted: #7d8a96;
    --accent: #2aa6c9;
    --avatar: #d3d9dc;
  }
  * { margin: 0; padding: 0; box-sizing: border-box; }
  html, body { width: 856px; height: 1200px; overflow: hidden; background: var(--white); }
  .flyer { position: relative; width: 856px; height: 1200px; background: var(--white); font-family: "Montserrat", sans-serif; color: var(--navy); }
  .header-panel { position: absolute; left: 26px; top: 0; width: 804px; height: 437px; background: var(--panel); }
  .brand { position: absolute; left: 71px; top: 64px; color: var(--white); }
  .brand-name { font-size: 27px; font-weight: 700; letter-spacing: 0.5px; line-height: 1; }
  .brand-slogan { font-size: 9px; font-weight: 400; margin-top: 5px; opacity: 0.8; }
  .hero-photo { position: absolute; left: 38px; top: 189px; width: 778px; height: 263px;
    background: radial-gradient(ellipse at 50% 45%, #e9e4d8 0%, #b9b6ad 30%, #6f6c66 65%, #4a4845 100%); }
  .hero-photo::after { content: ""; position: absolute; left: 60px; right: 60px; bottom: 0; height: 80px;
    background: linear-gradient(180deg, rgba(226,165,130,0.0), rgba(214,150,112,0.75)); }
  .title { position: absolute; left: 72px; top: 503px; font-size: 50px; font-weight: 500; letter-spacing: 0.3px; line-height: 1; }
  .title-rule { position: absolute; left: 72px; top: 568px; width: 33px; height: 2px; background: var(--navy); }
  .subtitle { position: absolute; left: 71px; top: 577px; font-size: 21.5px; font-weight: 500; color: #1b2b44; white-space: nowrap; }
  .details-panel { position: absolute; left: 0; top: 638px; width: 856px; height: 344px; background: var(--panel); }
  .section-heading { position: absolute; left: 82px; top: 656px; font-size: 22px; font-weight: 500; line-height: 1.22; }
  .section-rule { position: absolute; left: 76px; top: 713px; width: 34px; height: 2px; background: var(--navy); }
  .topics { position: absolute; left: 90px; top: 737px; list-style: none; font-family: "Open Sans", sans-serif; font-size: 10.6px; color: var(--ink); line-height: 19.6px; white-space: nowrap; }
  .info-item { position: absolute; left: 457px; }
  .info-icon { position: absolute; left: 0; top: 0; width: 40px; height: 40px; background: var(--navy); }
  .info-label { position: absolute; left: 53px; top: -2px; font-size: 14.5px; font-weight: 500; white-space: nowrap; }
  .info-text { position: absolute; left: 54px; top: 26px; width: 310px; font-size: 11.8px; color: var(--ink); line-height: 17px; }
  .info-when { top: 697px; }
  .info-when .info-label { top: 0; }
  .info-where { top: 784px; }
  .info-program { top: 869px; }
  .hosts-tag { position: absolute; left: 71px; top: 962px; width: 107px; height: 39px; background: var(--navy); color: var(--white); font-size: 27px; font-weight: 500; text-align: center; line-height: 40px; }
  .host { position: absolute; top: 1041px; display: flex; gap: 12px; }
  .host-avatar { flex: none; width: 80px; height: 80px; border-radius: 50%; background: var(--avatar); }
  .host-info { margin-top: -1px; }
  .host-name { font-size: 13.5px; font-weight: 500; color: var(--ink); white-space: nowrap; line-height: 18px; }
  .host-bio { margin-top: 5px; font-size: 10.6px; color: var(--muted); line-height: 17px; }
  .host-contact { margin-top: 3px; font-size: 9.2px; color: var(--accent); white-space: nowrap; }
  .host-one { left: 70px; }
  .host-one .host-bio { width: 240px; }
  .host-two { left: 457px; }
  .host-two .host-bio { width: 290px; }
  .footer-band { position: absolute; left: 71px; top: 1176px; width: 714px; height: 24px; background: var(--navy); }
</style>
</head>
<body>
<main class="flyer">
  <div class="header-panel"></div>
  <div class="brand">
    <div class="brand-name">YOUR LOGO</div>
    <div class="brand-slogan">Slogan Company Here</div>
  </div>
  <div class="hero-photo" role="img" aria-label="Photo of a small model house resting on a stack of banknotes"></div>

  <h1 class="title">LIVE EVENT</h1>
  <div class="title-rule"></div>
  <p class="subtitle">Learn How To Make Big Money with Foreclosure Auctions</p>

  <section class="details-panel"></section>
  <h2 class="section-heading">WHAT<br>TO EXPECT</h2>
  <div class="section-rule"></div>
  <ul class="topics">
    <li>How To Search Properties on County Site</li>
    <li>How To Determine If The Property Is Worth Further Research</li>
    <li>How To Navigate From KEYSTONE GRAB Site to 3rd Party Sites</li>
    <li>How To Find Total HOA Assessments</li>
    <li>How To Find Total Mortgage Debt</li>
    <li>How To Find Taxes Due</li>
    <li>How To Find Other Foreclosure Cases</li>
    <li>How To Determine Market Value</li>
    <li>How To Find Other Liens</li>
    <li>How To Search Properties on Gavelor AI</li>
    <li>Why You Should Order Report</li>
  </ul>

  <div class="info-item info-when">
    <div class="info-icon"></div>
    <div class="info-label">WHEN</div>
    <p class="info-text">3/16-3/18 3/23-3/25, 3/30-4/1</p>
  </div>
  <div class="info-item info-where">
    <div class="info-icon"></div>
    <div class="info-label">WHERE</div>
    <p class="info-text">Lorem ipsum dolor sit amet, consectetur adipiscing elit. Praesent sollicitudin, mi et</p>
  </div>
  <div class="info-item info-program">
    <div class="info-icon"></div>
    <div class="info-label">PROGRAM</div>
    <p class="info-text">Day 1 - Property Research<br>Day 2 - Property Management<br>Day 3 - Gavelor AI Demo, KEYSTONE GRAB Members, BricklineHoldings TV Coaching Packages</p>
  </div>

  <div class="hosts-tag">HOSTS</div>
  <div class="host host-one">
    <div class="host-avatar" role="img" aria-label="Portrait of host Dalton Preswick"></div>
    <div class="host-info">
      <div class="host-name">Dalton Preswick</div>
      <p class="host-bio">Real Estate Investor since 2001 flipped over 100 properties.</p>
      <p class="host-contact">+1 123 456 7890 &nbsp;|&nbsp; dalton@preswick.example</p>
    </div>
  </div>
  <div class="host host-two">
    <div class="host-avatar" role="img" aria-label="Portrait of host Owen Lathey"></div>
    <div class="host-info">
      <div class="host-name">Owen Lathey</div>
      <p class="host-bio">Founder of KEYSTONE GRAB &amp; Real Estate Auction Buyer Since 2011 Buying over 350 Properties</p>
      <p class="host-contact">+1 123 456 7890 &nbsp;|&nbsp; owen@lathey.example</p>
    </div>
  </div>

  <div class="footer-band"></div>
</main>
</body>
</html>
```